Design business card for Bright Harbour Coaching!

I am a personal development coach (like a life coach) and corporate trainer and need a professionally designed double sided business card.

It needs to contain the business logo (I'm happy for the designer to choose the layout of the logo as I am still working out the best option myself) and the following information:

Corinne Vashti
Personal Development Coach and Trainer

+61 (0)452 918 637 (written that way)
corinne@bright-harbour.example

www.bright-harbour.example

```html
<!DOCTYPE html>
<html lang="en">
<head>
<meta charset="utf-8">
<title>Bright Harbour Coaching – Business Card</title>
<link rel="stylesheet" href="https://fonts.googleapis.com/css2?family=Cinzel:wght@400&family=Arimo:wght@400;700&display=swap">
<style>
  :root {
    --teal: #1697a3;
    --teal-deep: #0e7f8a;
    --teal-light: #5fc0c8;
    --paper: #ffffff;
    --ink: #1e1e1e;
    --logo-grey: #6d6f72;
    --backdrop: #e9ecee;
  }
  * { margin: 0; padding: 0; box-sizing: border-box; }
  html, body { width: 1200px; height: 950px; overflow: hidden; }
  body { background: var(--backdrop); position: relative; font-family: "Arimo", Arial, sans-serif; }

  .card {
    position: absolute;
    width: 680px;
    height: 416px;
    overflow: hidden;
    box-shadow: 0 10px 28px rgba(0,0,0,0.18);
  }
  .card--front { left: 120px; top: 40px; background: var(--teal); }
  .card--back { left: 400px; top: 494px; background: var(--paper); }

  /* front */
  .brand {
    position: absolute;
    left: 0; right: 0; top: 150px;
    display: flex; align-items: center; justify-content: center; gap: 14px;
  }
  .brand__dot { width: 22px; height: 22px; border-radius: 50%; }
  .brand__name {
    font-family: "Cinzel", "Times New Roman", serif;
    font-weight: 400;
    font-size: 34px;
    letter-spacing: 0.5px;
    white-space: nowrap;
  }
  .card--front .brand__dot { background: var(--paper); }
  .card--front .brand__name { color: var(--paper); }

  .front-web {
    position: absolute;
    left: 0; right: 0; top: 236px;
    display: flex; align-items: center; justify-content: center; gap: 12px;
    color: var(--paper);
    font-size: 17px;
    letter-spacing: 3px;
  }
  .front-web__rule { width: 90px; height: 1px; background: rgba(255,255,255,0.8); }

  /* back */
  .back-waves { position: absolute; inset: 0; }
  .holder {
    position: absolute; right: 36px; top: 26px;
    text-align: right; color: var(--paper);
  }
  .holder__name { font-weight: 700; font-size: 23px; }
  .holder__role { font-size: 16px; line-height: 22px; margin-top: 4px; }

  .card--back .brand { left: 130px; right: auto; top: 212px; justify-content: flex-start; }
  .card--back .brand__dot { background: var(--teal); }
  .card--back .brand__name { color: var(--logo-grey); font-size: 30px; }

  .contact {
    position: absolute; left: 150px; top: 300px;
    color: var(--ink); font-size: 17px; line-height: 25px;
    list-style: none;
  }
</style>
</head>
<body>

<section class="card card--front" aria-label="Card front">
  <div class="brand">
    <span class="brand__dot"></span>
    <span class="brand__name">Bright Harbour Coaching</span>
  </div>
  <div class="front-web">
    <span class="front-web__rule"></span>
    <span>www.bright-harbour.example</span>
    <span class="front-web__rule"></span>
  </div>
</section>

<section class="card card--back" aria-label="Card back">
  <svg class="back-waves" viewBox="0 0 680 416" width="680" height="416" aria-hidden="true">
    <path d="M0,0 H680 V120 C560,118 420,132 310,150 C190,170 70,215 0,300 Z" fill="var(--teal)"/>
    <path d="M680,120 C560,118 420,132 310,150 C420,140 560,138 680,150 Z" fill="var(--teal-deep)"/>
    <path d="M0,300 C60,225 170,182 300,160 C190,192 95,240 40,320 C25,345 12,370 0,390 Z" fill="var(--teal-deep)"/>
    <path d="M0,390 C25,330 70,270 130,235 C80,280 40,330 18,416 H0 Z" fill="var(--teal-light)"/>
  </svg>

  <div class="holder">
    <p class="holder__name">Corinne Vashti</p>
    <p class="holder__role">Personal Development<br>Coach &amp; Trainer</p>
  </div>

  <div class="brand">
    <span class="brand__dot"></span>
    <span class="brand__name">Bright Harbour Coaching</span>
  </div>

  <ul class="contact">
    <li>+61 (0)452 918 637</li>
    <li>corinne@bright-harbour.example</li>
    <li>www.bright-harbour.example</li>
  </ul>
</section>

</body>
</html>
```